Business Card Design

My business is writing crime novels to entertain readers. I write legal thrillers and mysteries. I need a card for publishers, agents, other authors, and media.

Industry/Entity Type

Legal

Contact Information for Business Card

Paul Trenholt
www.trenholtnoir.example
pbtrenholt@mailbox.example
0064 27 5170942

```html
<!DOCTYPE html>
<html lang="en">
<head>
<meta charset="utf-8">
<title>Paul Trenholt – Business Card</title>
<link rel="stylesheet" href="https://fonts.googleapis.com/css2?family=Open+Sans:wght@400;600&display=swap">
<style>
  :root {
    --backdrop: #ececec;
    --card-base: #1f3231;
    --card-deep: #152322;
    --card-glow: #2f4a48;
    --ink: #ffffff;
    --portrait-skin: #8a5d4c;
    --portrait-dark: #1a1a1a;
    --portrait-shirt: #d9d3cf;
  }
  * { margin: 0; padding: 0; box-sizing: border-box; }
  html, body {
    width: 1200px;
    height: 800px;
    overflow: hidden;
    background: var(--backdrop);
  }
  .canvas {
    width: 1200px;
    height: 800px;
    display: flex;
    align-items: center;
    justify-content: center;
  }
  .business-card {
    position: relative;
    width: 1050px;
    height: 600px;
    overflow: hidden;
    background:
      radial-gradient(ellipse at 38% 22%, var(--card-glow) 0%, transparent 45%),
      radial-gradient(ellipse at 75% 80%, var(--card-glow) 0%, transparent 40%),
      radial-gradient(ellipse at 12% 85%, var(--card-deep) 0%, transparent 50%),
      var(--card-base);
    box-shadow: 0 6px 18px rgba(0,0,0,0.18);
  }
  .contact-block {
    position: absolute;
    left: 315px;
    top: 210px;
    transform: translateX(-50%);
    text-align: center;
    color: var(--ink);
    font-family: "Open Sans", Arial, sans-serif;
    white-space: nowrap;
  }
  .contact-name {
    font-size: 40px;
    font-weight: 600;
    font-variant: small-caps;
    letter-spacing: 5px;
    margin-bottom: 14px;
  }
  .contact-line {
    font-size: 23px;
    font-weight: 600;
    letter-spacing: 0.6px;
    line-height: 38px;
  }
  .author-portrait {
    position: absolute;
    right: 0;
    bottom: 0;
    width: 560px;
    height: 600px;
    background:
      radial-gradient(ellipse 30% 34% at 58% 38%, var(--portrait-skin) 0%, rgba(138,93,76,0.6) 55%, transparent 100%),
      radial-gradient(ellipse 14% 18% at 56% 92%, var(--portrait-shirt) 0%, transparent 100%),
      radial-gradient(ellipse 60% 30% at 56% 100%, var(--portrait-dark) 0%, rgba(26,26,26,0.7) 60%, transparent 100%);
  }
</style>
</head>
<body>
  <main class="canvas">
    <section class="business-card">
      <div class="contact-block">
        <h1 class="contact-name">Paul Trenholt</h1>
        <p class="contact-line">www.trenholtnoir.example</p>
        <p class="contact-line">pbtrenholt@mailbox.example</p>
        <p class="contact-line">0064 27 5170942</p>
      </div>
      <div class="author-portrait" role="img" aria-label="Portrait photograph of the author in a dark jacket and white shirt"></div>
    </section>
  </main>
</body>
</html>
```